Business Card Design

Looking for a clean professional Business card design with our logo. Needs to be able to customize name, address and contact info so we can use it multiple times with different people, please.

```html
<!DOCTYPE html>
<html lang="en">
<head>
<meta charset="UTF-8">
<title>Brightpath Careers – Business Card</title>
<link href="https://fonts.googleapis.com/css2?family=Montserrat:wght@400;500;600&display=swap" rel="stylesheet">
<style>
  :root {
    --brand-red: #c41f2e;
    --ink: #333336;
    --paper: #ffffff;
    --backdrop: #e6e7ea;
  }
  * { box-sizing: border-box; margin: 0; padding: 0; }
  html, body {
    width: 1200px;
    height: 900px;
    overflow: hidden;
    background: var(--backdrop);
    font-family: "Montserrat", sans-serif;
    color: var(--ink);
  }
  .sheet {
    width: 1200px;
    height: 900px;
    display: flex;
    flex-direction: column;
    align-items: center;
    justify-content: center;
    gap: 48px;
  }
  .card {
    position: relative;
    width: 660px;
    height: 378px;
    border-radius: 28px;
    background: var(--paper);
    overflow: hidden;
    box-shadow: 0 10px 30px rgba(0,0,0,0.12);
  }

  /* Back side */
  .card-back {
    display: flex;
    flex-direction: column;
    align-items: center;
    justify-content: center;
  }
  .tab {
    position: absolute;
    width: 44px;
    height: 58px;
    background: var(--brand-red);
  }
  .tab-right { right: 0; top: 40px; border-radius: 24px 0 0 24px; }
  .tab-left { left: 0; bottom: 82px; border-radius: 0 24px 24px 0; }

  .brand {
    display: flex;
    align-items: center;
    gap: 14px;
  }
  .brand-square {
    width: 54px;
    height: 54px;
    background: var(--brand-red);
  }
  .brand-name {
    font-weight: 600;
    font-size: 26px;
    letter-spacing: 0.5px;
    line-height: 1.1;
    color: var(--brand-red);
    text-transform: uppercase;
  }
  .card-back .brand { margin-top: -10px; }
  .back-website {
    position: absolute;
    bottom: 78px;
    font-size: 17px;
    font-weight: 500;
    letter-spacing: 0.3px;
  }

  /* Front side */
  .card-front {
    display: grid;
    grid-template-columns: 49% 51%;
  }
  .front-panel {
    background: var(--brand-red);
    display: flex;
    align-items: center;
    justify-content: center;
  }
  .front-panel .brand-square { background: var(--ink); }
  .front-panel .brand-name { color: var(--paper); font-size: 22px; }

  .front-details {
    padding: 52px 34px 0 40px;
  }
  .holder-name {
    font-size: 25px;
    font-weight: 500;
    color: var(--brand-red);
    line-height: 1.1;
  }
  .holder-role {
    font-size: 21px;
    font-weight: 500;
    margin-bottom: 32px;
  }
  .contact-list { list-style: none; }
  .contact-item {
    display: flex;
    align-items: center;
    gap: 14px;
    font-size: 16px;
    font-weight: 500;
    height: 34px;
  }
  .contact-icon {
    width: 22px;
    height: 22px;
    flex: none;
    fill: var(--ink);
  }
</style>
</head>
<body>
<main class="sheet">

  <section class="card card-back" aria-label="Business card back">
    <span class="tab tab-right"></span>
    <span class="tab tab-left"></span>
    <div class="brand">
      <span class="brand-square"></span>
      <span class="brand-name">Brightpath Careers</span>
    </div>
    <p class="back-website">www.yourwebsite.com</p>
  </section>

  <section class="card card-front" aria-label="Business card front">
    <div class="front-panel">
      <div class="brand">
        <span class="brand-square"></span>
        <span class="brand-name">Brightpath Careers</span>
      </div>
    </div>
    <div class="front-details">
      <h1 class="holder-name">Marcus Ellery</h1>
      <p class="holder-role">Director</p>
      <ul class="contact-list">
        <li class="contact-item">
          <svg class="contact-icon" viewBox="0 0 24 24" aria-hidden="true"><path d="M6.6 10.8a15.1 15.1 0 0 0 6.6 6.6l2.2-2.2c.3-.3.7-.4 1-.2 1.1.4 2.3.6 3.6.6.6 0 1 .4 1 1V20c0 .6-.4 1-1 1A17 17 0 0 1 3 4c0-.6.4-1 1-1h3.5c.6 0 1 .4 1 1 0 1.3.2 2.5.6 3.6.1.3 0 .7-.2 1z"/></svg>
          <span>000 000 0000</span>
        </li>
        <li class="contact-item">
          <svg class="contact-icon" viewBox="0 0 24 24" aria-hidden="true"><path d="M2 5h20v14H2zm2 2v.4l8 5.2 8-5.2V7zm0 2.8V17h16V9.8l-8 5.2z"/></svg>
          <span>info@yourmail.com</span>
        </li>
        <li class="contact-item">
          <svg class="contact-icon" viewBox="0 0 24 24" aria-hidden="true"><path d="M12 2a10 10 0 1 0 0 20 10 10 0 0 0 0-20zm6.9 6h-3a15 15 0 0 0-1.3-3.9A8 8 0 0 1 18.9 8zM12 4c.9 1.2 1.6 2.5 2 4h-4c.4-1.5 1.1-2.8 2-4zM4.3 14a8 8 0 0 1 0-4h3.4a16 16 0 0 0 0 4zm.8 2h3a15 15 0 0 0 1.3 3.9A8 8 0 0 1 5.1 16zm3-8h-3a8 8 0 0 1 4.3-3.9C8.8 5.3 8.4 6.6 8.1 8zM12 20c-.9-1.2-1.6-2.5-2-4h4c-.4 1.5-1.1 2.8-2 4zm2.3-6H9.7a14 14 0 0 1 0-4h4.6a14 14 0 0 1 0 4zm.3 5.9c.6-1.2 1-2.5 1.3-3.9h3a8 8 0 0 1-4.3 3.9zm1.7-5.9a16 16 0 0 0 0-4h3.4a8 8 0 0 1 0 4z"/></svg>
          <span>www.yourwebsite.com</span>
        </li>
        <li class="contact-item">
          <svg class="contact-icon" viewBox="0 0 24 24" aria-hidden="true"><path d="M12 2a7 7 0 0 0-7 7c0 5.2 7 13 7 13s7-7.8 7-13a7 7 0 0 0-7-7zm0 9.5A2.5 2.5 0 1 1 12 6.5a2.5 2.5 0 0 1 0 5z"/></svg>
          <span>Riverton 84065</span>
        </li>
      </ul>
    </div>
  </section>

</main>
</body>
</html>
```